Premium Business Cards

Hi
I need 5 premium business cards for my clients, and need very urgent.
Requirements:
1. Simple
2. Professional
3. Black /Dark
Our client product is Premium Tuxedo Clothing, for privacy reason, we are unable to upload their logo, sorry.

Target Market(s)

Top level customer, aged 35 to 60 European.

Industry/Entity Type

Business

Font styles to use
Script

Requirements
Must have
• The business cards must in dark theme, our logo color is metal yellow and white gold.
Size 90mmx55mm double sided.
Should not have
• Don't like fancy color or bright color.

```html
<!DOCTYPE html>
<html lang="en">
<head>
<meta charset="utf-8">
<title>Business Card – Front and Back</title>
<link rel="stylesheet" href="https://fonts.googleapis.com/css2?family=Playball&family=Petit+Formal+Script&display=swap">
<style>
  :root {
    --page: #ffffff;
    --ink: #000000;
    --card-black: #050505;
    --card-text: #f4ead0;
    --white-gold: #efe3c2;
    --metal-gold: #b8913a;
    --gold-deep: #6e5420;
    --bronze-dark: #2a1f0c;
    --band-gold: #a8842f;
    --band-text: #0b0905;
    --label-font: "Playball", cursive;
    --card-font: "Petit Formal Script", cursive;
  }
  html, body {
    margin: 0;
    padding: 0;
    overflow: hidden;
    background: var(--page);
  }
  .sheet {
    position: relative;
    width: 1200px;
    height: 900px;
    background: var(--page);
    overflow: hidden;
  }
  .side-label {
    position: absolute;
    margin: 0;
    font-family: var(--label-font);
    font-weight: 400;
    color: var(--ink);
    line-height: 1;
  }
  .side-label--front { left: 766px; top: 102px; font-size: 112px; }
  .side-label--back  { left: 90px;  top: 625px; font-size: 118px; }

  .card {
    position: absolute;
    width: 619px;
    height: 356px;
    background: var(--card-black);
    overflow: hidden;
    color: var(--card-text);
    font-family: var(--card-font);
  }
  .card--front { left: 63px; top: 37px; }
  .card--back  { left: 519px; top: 512px; }

  .card__art {
    position: absolute;
    inset: 0;
  }

  .front-text {
    position: absolute;
    left: 462px;
    top: 38px;
    width: 150px;
    font-size: 14px;
    line-height: 30px;
    white-space: nowrap;
  }
  .front-text p { margin: 0; }
  .front-text__person {
    margin-top: 34px;
    text-align: center;
    padding-right: 30px;
    line-height: 28px;
  }
  .front-text__contact { margin-top: 44px; }

  .back-details {
    position: absolute;
    left: 24px;
    top: 71px;
  }
  .back-details__title {
    margin: 0 0 24px;
    font-size: 15px;
    font-weight: 700;
    line-height: 20px;
  }
  .back-details__line {
    display: block;
    height: 0;
    border-top: 2px dotted var(--white-gold);
    margin-bottom: 28px;
  }
  .back-details__line--1 { width: 131px; }
  .back-details__line--2 { width: 120px; }
  .back-details__line--3 { width: 82px; }

  .web-band {
    position: absolute;
    left: 0;
    bottom: 0;
    width: 100%;
    height: 21px;
    background: linear-gradient(90deg, var(--gold-deep), var(--band-gold) 50%, var(--gold-deep));
    color: var(--band-text);
    text-align: center;
    font-size: 12px;
    font-weight: 700;
    line-height: 21px;
    letter-spacing: 0.5px;
  }
</style>
</head>
<body>
<main class="sheet">
  <h2 class="side-label side-label--front">Front</h2>

  <section class="card card--front">
    <svg class="card__art" width="619" height="356" viewBox="0 0 619 356" role="img" aria-label="Abstract burst of dotted swirls and halftone circles in dark gold filling the left of the card">
      <defs>
        <radialGradient id="front-burst" cx="0.3" cy="0.6" r="0.7">
          <stop offset="0" stop-color="var(--metal-gold)" stop-opacity="0.55"/>
          <stop offset="0.45" stop-color="var(--gold-deep)" stop-opacity="0.55"/>
          <stop offset="0.8" stop-color="var(--bronze-dark)"/>
          <stop offset="1" stop-color="var(--card-black)"/>
        </radialGradient>
      </defs>
      <rect width="619" height="356" fill="var(--card-black)"/>
      <rect width="619" height="356" fill="url(#front-burst)"/>
    </svg>
    <div class="front-text">
      <p>Company logo</p>
      <p>or Company name</p>
      <div class="front-text__person">
        <p>Your Name</p>
        <p>(Your title)</p>
      </div>
      <div class="front-text__contact">
        <p>your address</p>
        <p>phone no: and etc.</p>
      </div>
    </div>
  </section>

  <h2 class="side-label side-label--back">Back</h2>

  <section class="card card--back">
    <svg class="card__art" width="619" height="356" viewBox="0 0 619 356" role="img" aria-label="Floral swirls with soft glowing circles and sparkles in dark gold on the right of the card">
      <defs>
        <radialGradient id="back-glow" cx="0.75" cy="0.6" r="0.55">
          <stop offset="0" stop-color="var(--gold-deep)" stop-opacity="0.75"/>
          <stop offset="0.55" stop-color="var(--bronze-dark)"/>
          <stop offset="1" stop-color="var(--card-black)"/>
        </radialGradient>
      </defs>
      <rect width="619" height="356" fill="var(--card-black)"/>
      <rect width="619" height="356" fill="url(#back-glow)"/>
    </svg>
    <div class="back-details">
      <p class="back-details__title">Any your details</p>
      <span class="back-details__line back-details__line--1"></span>
      <span class="back-details__line back-details__line--2"></span>
      <span class="back-details__line back-details__line--3"></span>
    </div>
    <div class="web-band">visit www.yourcompany.com</div>
  </section>
</main>
</body>
</html>
```